Kveldbrá - Start-up company selling electricity

Hello let me tell you about Kveldbrá.

Kveldbrá is start-up company selling electricity in Iceland. The operations of the company consist of making power usage forecasts for our customers, purchasing the electricity wholesale from the energy producers, and selling the electricity to the consumer. We are focused on tech by using optimization and machine learning to minimize electricity prices to our customers. Our marketing strategy is to portray a tech company mindset and to show dedication to driving down the electricity price on the market.

We need your help to make our website pop. Possible concepts to work with are as follows:

- Iceland the land of ice and fire
- Green energy
- Innovation
- Tech and data science

Link to our website: https://prufa.kveldbra.is/
We are open to ideas.
Thank you!

Target Market(s)

Electricity consumers both homes and companies.

Number of Pages Required

1 page

Font styles to use
Serif
Sans Serif

```html
<!DOCTYPE html>
<html lang="en">
<head>
<meta charset="utf-8">
<title>Kveldbrá – Electricity at the best price</title>
<link href="https://fonts.googleapis.com/css2?family=Archivo:wght@400;500;700;800&family=Montserrat:wght@400;500&family=Noto+Sans:wght@400;600;700&family=Roboto:wght@400;500;700&display=swap" rel="stylesheet">
<style>
:root{
  --navy:#173a5e;
  --green:#0a7a0a;
  --gray-bg:#e9eaea;
  --yellow:#fcd000;
  --faq-bg:#d7e8ef;
  --faq-item:#e1eaef;
  --qmark:#b9ccd9;
  --footer:#666666;
  --white:#ffffff;
  --text-muted:#6b6b6b;
  --border:#a8adb2;
}
*{margin:0;padding:0;box-sizing:border-box}
html,body{width:1200px;height:3611px;overflow:hidden}
body{position:relative;background:var(--gray-bg);font-family:"Noto Sans",sans-serif;color:var(--navy)}
.abs{position:absolute}
.center{left:0;width:1200px;text-align:center}

/* header */
.site-header{top:0;left:0;width:1200px;height:105px;background:var(--white)}
.brand{left:132px;top:28px;display:flex;align-items:center;gap:10px}
.brand-dot{width:26px;height:26px;border-radius:50%;background:var(--navy)}
.brand-name{font-family:"Noto Sans",sans-serif;font-weight:700;font-size:30px;color:var(--green);letter-spacing:.5px}
.nav{top:36px;left:604px;display:flex;gap:38px;font-family:"Roboto",sans-serif;font-weight:500;font-size:17px;color:var(--navy)}
.nav a{color:inherit;text-decoration:none;display:flex;align-items:center;gap:6px}
.nav .active{color:var(--green);border-bottom:2px solid var(--green);padding-bottom:4px}
.login{left:937px;top:26px;width:131px;height:44px;border:2px solid var(--navy);border-radius:10px;display:flex;align-items:center;justify-content:space-between;padding:0 12px 0 16px;font-family:"Roboto",sans-serif;font-weight:500;font-size:17px}

/* hero */
.hero{top:105px;left:0;width:1200px;height:570px}
.hero-bg{position:absolute;inset:0;background:linear-gradient(180deg,#a8dcf3 0%,#8fd0ef 61%,#fcc500 61%,#fdb800 100%)}
.hero-bulb{position:absolute;left:660px;top:120px;width:340px;height:420px;border-radius:50% 50% 30% 30%;background:radial-gradient(circle at 50% 35%,rgba(255,255,255,.55),rgba(200,210,215,.35) 60%,rgba(160,160,160,0) 75%)}
.hero-kicker{left:132px;top:70px;font-family:"Archivo",sans-serif;font-size:51px;color:var(--green)}
.hero-line{left:132px;top:138px;font-family:"Archivo",sans-serif;font-size:42px;color:var(--navy)}
.hero-big{left:132px;top:185px;font-family:"Archivo",sans-serif;font-weight:800;font-size:74px;line-height:76px;color:var(--navy)}
.hero-big small{font-weight:400;font-size:42px}
.hero-text{left:132px;top:355px;width:690px;font-family:"Montserrat",sans-serif;font-size:20px;line-height:26px;color:var(--navy)}
.btn-join{left:132px;top:461px;width:176px;height:44px;background:var(--green);border:2px solid #065c06;border-radius:8px;color:var(--white);font-family:"Roboto",sans-serif;font-weight:700;font-size:16px;display:flex;align-items:center;justify-content:center}

/* shared */
.section-title{font-weight:700;font-size:43px}
.soft-btn{width:178px;height:46px;background:var(--gray-bg);border-radius:8px;box-shadow:0 4px 8px rgba(0,0,0,.18);font-family:"Roboto",sans-serif;font-size:16px;color:var(--navy);display:flex;align-items:center;justify-content:center}
.small-copy{font-family:"Montserrat",sans-serif;font-size:14px;line-height:20px;color:#333}

/* services */
.service-icon{width:140px;height:140px;border-radius:50%;background:#efefef;box-shadow:0 6px 10px rgba(0,0,0,.2);display:flex;align-items:center;justify-content:center}
.service-title{font-weight:700;font-size:21px}
.service-text{width:340px;font-size:15px;line-height:23px;color:var(--text-muted)}

/* price */
.price-band{top:1647px;left:0;width:1200px;height:600px;background:var(--yellow)}
.price-num{font-weight:700;font-size:130px;line-height:130px;color:var(--navy);letter-spacing:-2px}
.price-unit{font-weight:700;font-size:27px;line-height:36px}
.btn-compare{left:511px;top:2143px;width:178px;height:44px;background:var(--yellow);border-radius:8px;box-shadow:0 3px 10px rgba(180,120,0,.5);font-family:"Roboto",sans-serif;font-size:16px;display:flex;align-items:center;justify-content:center}

/* faq */
.faq{top:2247px;left:0;width:1200px;height:790px;background:var(--faq-bg)}
.faq-item{left:132px;width:598px;height:56px;background:var(--faq-item);border-radius:10px;box-shadow:0 3px 6px rgba(0,0,0,.08);display:flex;align-items:center;justify-content:space-between;padding:0 18px 0 30px;font-weight:600;font-size:21px}
.qmark{left:830px;top:2490px;font-weight:700;font-size:440px;line-height:440px;color:var(--qmark)}

/* contact */
.field{border:1px solid var(--border);border-radius:3px;font-family:"Roboto",sans-serif;font-size:15px;color:#9a9fa4;padding:12px 20px}
.contact-line{left:132px;display:flex;align-items:center;gap:10px;font-family:"Montserrat",sans-serif;font-size:18px;color:#111}
.address{left:162px;top:3415px;width:230px;font-size:15px;line-height:23px;color:var(--text-muted)}

/* footer */
.site-footer{top:3540px;left:0;width:1200px;height:71px;background:var(--footer);color:var(--white);font-weight:700;font-size:11px}
</style>
</head>
<body>

<header class="abs site-header">
  <div class="abs brand"><span class="brand-dot"></span><span class="brand-name">KVELDBRÁ</span></div>
  <nav class="abs nav">
    <a class="active" href="#"><svg width="16" height="16" viewBox="0 0 16 16"><path d="M8 1 1 8h2v7h4v-4h2v4h4V8h2z" fill="#0a7a0a"/></svg>HOME</a>
    <a href="#">ABOUT</a>
    <a href="#">CONTACT</a>
  </nav>
  <div class="abs login">LOGIN
    <svg width="28" height="28" viewBox="0 0 28 28"><circle cx="14" cy="14" r="13" fill="#173a5e"/><circle cx="14" cy="11" r="4.5" fill="#fff"/><path d="M6 22c2-4 5-5 8-5s6 1 8 5" fill="#fff"/></svg>
  </div>
</header>

<section class="abs hero">
  <div class="hero-bg" role="img" aria-label="Photo of a clear light bulb standing on a sky blue and yellow background"></div>
  <div class="hero-bulb"></div>
  <div class="abs hero-kicker">ELECTRICITY</div>
  <div class="abs hero-line">at the best price for</div>
  <div class="abs hero-big">Residence <small>and</small><br>commercial</div>
  <p class="abs hero-text">Let's make the electricity system smarter together. Kveldbrá uses artificial intelligence, data science and automation to minimize costs and promote eccentricity</p>
  <div class="abs btn-join">JOIN US TODAY</div>
</section>

<h2 class="abs center section-title" style="top:738px">About Kveldbrá</h2>
<p class="abs small-copy" style="left:280px;top:828px;width:640px;text-align:center">Kveldbrá uses automation and artificial intelligence to achieve lower prices in the electricity market. Our goal is to minimize the cost of energy sales, promote energy balance and offer good service.</p>
<div class="abs soft-btn" style="left:511px;top:920px">Read More</div>

<h2 class="abs center section-title" style="top:1062px">Services we provide</h2>
<p class="abs small-copy" style="left:255px;top:1124px;width:690px;text-align:center">Our marketing strategy is to portray a tech company mindset and to show dedication to driving down the electricity price on the market.</p>

<div class="abs service-icon" style="left:260px;top:1210px">
  <svg width="90" height="82" viewBox="0 0 90 82"><path d="M45 4 2 42h12v38h62V42h12L70 26V8H60v9z" fill="#0a7a0a"/><path d="M36 78 50 58H40l10-16" stroke="#efefef" stroke-width="6" fill="none"/></svg>
</div>
<div class="abs service-icon" style="left:689px;top:1213px">
  <svg width="90" height="74" viewBox="0 0 90 74"><path d="M4 24 45 2l41 22v48H4z" fill="#0a7a0a"/><rect x="18" y="30" width="54" height="42" fill="#efefef"/><rect x="22" y="34" width="46" height="7" fill="#0a7a0a"/><rect x="22" y="45" width="46" height="7" fill="#0a7a0a"/><rect x="22" y="56" width="46" height="7" fill="#0a7a0a"/></svg>
</div>
<h3 class="abs service-title" style="left:260px;top:1390px">Kveldbrá for Home</h3>
<h3 class="abs service-title" style="left:689px;top:1390px">Kveldbrá for Business</h3>
<p class="abs service-text" style="left:260px;top:1426px">Lorem ipsum dolor sit amet, consectetur adipisicing elit, sed do eiusmod tempor incididunt ut labore et dolore magna aliqua.</p>
<p class="abs service-text" style="left:689px;top:1426px">Lorem ipsum dolor sit amet, consectetur adipisicing elit, sed do eiusmod tempor incididunt ut labore et dolore magna aliqua.</p>
<div class="abs soft-btn" style="left:260px;top:1518px">Register Now</div>
<div class="abs soft-btn" style="left:689px;top:1518px">Register Now</div>

<section class="abs price-band"></section>
<h2 class="abs center section-title" style="top:1720px">Our Best Price</h2>
<div class="abs price-num" style="left:190px;top:1825px">6.98</div>
<div class="abs price-unit" style="left:193px;top:1975px">ISK / kWh</div>
<div class="abs price-num" style="left:736px;top:1825px">6.25</div>
<div class="abs price-unit" style="left:739px;top:1975px">ISK / kWh<br>electric acceleration</div>
<div class="abs center" style="top:2094px;font-weight:700;font-size:21px">Make a price comparison</div>
<div class="abs btn-compare">Verðvaki</div>

<section class="abs faq"></section>
<div class="abs qmark">?</div>
<h2 class="abs center section-title" style="top:2335px">Frequently Asked Questions (FAQ)</h2>
<div class="abs faq-item" style="top:2458px">Can anyone buy electricity from Kveldbrá?<svg width="30" height="30" viewBox="0 0 30 30"><circle cx="15" cy="15" r="13" fill="none" stroke="#173a5e" stroke-width="2"/><path d="M15 8v14M8 15h14" stroke="#173a5e" stroke-width="2"/></svg></div>
<div class="abs faq-item" style="top:2546px">How do I buy electricity from Kveldbrá?<svg width="30" height="30" viewBox="0 0 30 30"><circle cx="15" cy="15" r="13" fill="none" stroke="#173a5e" stroke-width="2"/><path d="M15 8v14M8 15h14" stroke="#173a5e" stroke-width="2"/></svg></div>
<div class="abs faq-item" style="top:2635px">What happens after I sign up for a business?<svg width="30" height="30" viewBox="0 0 30 30"><circle cx="15" cy="15" r="13" fill="none" stroke="#173a5e" stroke-width="2"/><path d="M15 8v14M8 15h14" stroke="#173a5e" stroke-width="2"/></svg></div>
<div class="abs faq-item" style="top:2723px">The future with Kveldbrá?<svg width="30" height="30" viewBox="0 0 30 30"><circle cx="15" cy="15" r="13" fill="none" stroke="#173a5e" stroke-width="2"/><path d="M15 8v14M8 15h14" stroke="#173a5e" stroke-width="2"/></svg></div>
<div class="abs faq-item" style="top:2812px">How do I quit trading?<svg width="30" height="30" viewBox="0 0 30 30"><circle cx="15" cy="15" r="13" fill="none" stroke="#173a5e" stroke-width="2"/><path d="M15 8v14M8 15h14" stroke="#173a5e" stroke-width="2"/></svg></div>
<div class="abs faq-item" style="top:2900px">Does it cost to switch to Kveldbrá?<svg width="30" height="30" viewBox="0 0 30 30"><circle cx="15" cy="15" r="13" fill="none" stroke="#173a5e" stroke-width="2"/><path d="M15 8v14M8 15h14" stroke="#173a5e" stroke-width="2"/></svg></div>

<h2 class="abs center section-title" style="top:3125px">Still Do You Have Question?</h2>
<div class="abs" style="left:470px;top:3222px;font-weight:600;font-size:21px">Contact US</div>

<div class="abs contact-line" style="top:3290px">
  <svg width="26" height="20" viewBox="0 0 26 20"><rect x="1" y="1" width="24" height="18" fill="none" stroke="#111" stroke-width="2"/><path d="M1 1l12 10L25 1M1 19l9-9M25 19l-9-9" stroke="#111" stroke-width="2" fill="none"/></svg>kveldbra@kveldbra.is</div>
<div class="abs contact-line" style="top:3335px">
  <svg width="24" height="24" viewBox="0 0 24 24"><path d="M5 2l4 1 2 5-3 2c1 3 3 5 6 6l2-3 5 2 1 4c-1 2-3 3-5 3C10 21 3 14 2 6c0-2 1-3 3-4z" fill="#111"/></svg>555-0199</div>
<div class="abs contact-line" style="top:3380px">
  <svg width="20" height="26" viewBox="0 0 20 26"><path d="M10 1C5 1 1 5 1 10c0 6 9 15 9 15s9-9 9-15c0-5-4-9-9-9z" fill="#111"/><circle cx="10" cy="10" r="3.5" fill="#e9eaea"/></svg>Address:</div>
<p class="abs address">Lorem ipsum dolor sit amet, consectetur adipisicing elit, sed do</p>

<div class="abs field" style="left:470px;top:3290px;width:318px;height:43px">Name:</div>
<div class="abs field" style="left:798px;top:3290px;width:270px;height:43px">Phone:</div>
<div class="abs field" style="left:470px;top:3347px;width:598px;height:43px">E-mail:</div>
<div class="abs field" style="left:470px;top:3405px;width:598px;height:102px">Message:</div>

<footer class="abs site-footer">
  <span class="abs" style="left:128px;top:30px">© 2020 Mockup.&nbsp; All Rights Reserved.</span>
  <span class="abs" style="left:829px;top:30px">Privacy Policy</span>
  <span class="abs" style="left:975px;top:30px">Terms of Service</span>
</footer>

</body>
</html>
```